letterhead design

We have a business card with logo, ink etc and want to develop letterhead that uses the elements of the business card logo.
Must haves...and they should be designed in, not just plopped in :)
Dr. Lyle Varden
2817 W Marlow Street
Fresno, CA 93614
559-382-6157 p
559-382-7043 f
info@brindlespine.com
www.brindlespine.com
www.facebook.com/brindlespn
Updates

Rather than just have the logo on the page, is there someway to silkscreen it in the background to fill the page?

Reason: I was out of town for a week.

Industry/Entity Type

Business

Requirements
Nice to have
• I'd like the logo somehow silk screened in the background of the paper as well.

```html
<!DOCTYPE html>
<html lang="en">
<head>
<meta charset="utf-8">
<title>Brindle Spine Letterhead</title>
<link href="https://fonts.googleapis.com/css2?family=Lato:wght@400;700;900&display=swap" rel="stylesheet">
<style>
  :root {
    --navy: #0f2a4f;
    --ink: #1a2f52;
    --wash: #dbe1ea;
    --paper: #ffffff;
    --backdrop: #ffffff;
    --edge: #9a9a9a;
  }
  * { margin: 0; padding: 0; box-sizing: border-box; }
  html, body {
    width: 1200px;
    height: 900px;
    overflow: hidden;
    background: var(--backdrop);
    font-family: "Lato", sans-serif;
  }
  .sheet {
    position: absolute;
    left: 317px;
    top: 48px;
    width: 567px;
    height: 803px;
    background: var(--paper);
    border: 1px solid var(--edge);
    box-shadow: 3px 4px 4px rgba(0,0,0,0.35);
    overflow: hidden;
  }
  .background-mark {
    position: absolute;
    left: 40px;
    top: 600px;
    transform: rotate(-20deg);
    transform-origin: left top;
    color: var(--wash);
    font-weight: 900;
    font-size: 110px;
    line-height: 0.9;
    white-space: nowrap;
    pointer-events: none;
  }
  .background-mark .line-one { display: block; }
  .background-mark .line-two { display: block; margin-left: 150px; }
  .masthead {
    position: absolute;
    left: 33px;
    top: 60px;
    display: flex;
    align-items: flex-start;
    gap: 10px;
  }
  .brand {
    display: flex;
    align-items: center;
    gap: 6px;
    width: 140px;
    height: 52px;
  }
  .brand-square {
    width: 14px;
    height: 14px;
    background: var(--navy);
    flex: none;
  }
  .brand-name {
    color: var(--navy);
    font-weight: 900;
    font-size: 15px;
    letter-spacing: 0.5px;
    text-transform: uppercase;
    white-space: nowrap;
  }
  .contact {
    color: var(--ink);
    font-style: normal;
    font-size: 8px;
    line-height: 1.35;
    padding-top: 4px;
    white-space: nowrap;
  }
  .contact .doctor {
    font-weight: 700;
    font-size: 9px;
    color: var(--navy);
  }
  .footer-links {
    position: absolute;
    left: 33px;
    top: 733px;
    color: var(--ink);
    font-size: 7.5px;
    font-weight: 700;
    line-height: 1.45;
    list-style: none;
  }
</style>
</head>
<body>
  <main class="sheet">
    <div class="background-mark" aria-hidden="true">
      <span class="line-one">BRINDLE</span>
      <span class="line-two">SPINE</span>
    </div>

    <header class="masthead">
      <div class="brand">
        <span class="brand-square"></span>
        <span class="brand-name">Brindle Spine</span>
      </div>
      <address class="contact">
        <div class="doctor">Dr. Lyle Varden</div>
        <div>2817 W Marlow Street, Fresno, CA 93614</div>
        <div>Phone: 559-382-6157&nbsp;&nbsp;Fax: 559-382-7043</div>
      </address>
    </header>

    <ul class="footer-links">
      <li>info@brindlespine.com</li>
      <li>www.brindlespine.com</li>
      <li>www.friendloop.com/brindlespn</li>
    </ul>
  </main>
</body>
</html>
```